Plakat-Design für Kaminholz/Brennholz Verkauf
Zielgruppe
Kaminholz/Brennholz Verkauf - Zielgruppe Männer zwischen 35-65 Jahren, modernes Design
Aufgabenstellung
Das Plakat sollte modern und erschwinglich gestaltet sein. Es dient als Werbeplakat an einer Brücke über einer vielbefahrenden Straße und soll die Kunden zum Kaminholz Kauf anregen. Auffälliges Design. Design auch im vorbeifahren gut zu erkennen.
Maße 6,00m x 0,90m. Logo & Webseite: www.Ofenscheit-Lindqvist.de soll abgebildet sein.

```html
<!DOCTYPE html>
<html lang="de">
<head>
<meta charset="utf-8">
<title>Kaminholzhandel Lindqvist – Kamin- &amp; Brennholz</title>
<link href="https://fonts.googleapis.com/css2?family=Anton&family=Roboto+Condensed:wght@700&family=Montserrat:wght@400&display=swap" rel="stylesheet">
<style>
  :root {
    --ink: #0b0b0b;
    --white: #ffffff;
    --panel: rgba(236, 236, 236, 0.93);
    --price: #b9472b;
    --fire-dark: #120604;
    --fire-mid: #a8320c;
    --fire-hot: #f08a2c;
  }
  html, body {
    margin: 0;
    padding: 0;
    overflow: hidden;
    background: var(--ink);
  }
  .banner {
    position: relative;
    width: 1200px;
    height: 181px;
    overflow: hidden;
    font-family: "Anton", "Roboto Condensed", sans-serif;
  }
  .banner__flames {
    position: absolute;
    inset: 0;
    background:
      radial-gradient(ellipse 140px 90px at 60px 150px, rgba(240,138,44,0.75), transparent 70%),
      radial-gradient(ellipse 200px 120px at 320px 40px, rgba(200,70,20,0.8), transparent 70%),
      radial-gradient(ellipse 260px 130px at 620px 170px, rgba(240,120,40,0.85), transparent 70%),
      radial-gradient(ellipse 220px 110px at 880px 20px, rgba(220,90,25,0.8), transparent 70%),
      radial-gradient(ellipse 200px 120px at 1080px 90px, rgba(240,138,44,0.7), transparent 70%),
      radial-gradient(ellipse 160px 90px at 1170px 170px, rgba(168,50,12,0.8), transparent 70%),
      linear-gradient(90deg, var(--fire-dark), #3a1006 30%, var(--fire-dark) 60%, #2a0b05);
  }
  .brand {
    position: absolute;
    left: 20px;
    top: 14px;
    width: 250px;
    text-align: center;
    color: var(--white);
  }
  .brand__circle {
    display: block;
    margin: 0 auto;
    width: 90px;
    height: 90px;
  }
  .brand__name {
    margin: 8px 0 0;
    font-family: "Montserrat", sans-serif;
    font-weight: 400;
    font-size: 18px;
    line-height: 1;
  }
  .brand__tagline {
    margin: 8px 0 0;
    font-family: "Montserrat", sans-serif;
    font-size: 9px;
    line-height: 1;
  }
  .headline {
    position: absolute;
    left: 293px;
    top: 10px;
    width: 650px;
    height: 75px;
    background: var(--panel);
    color: var(--ink);
    font-size: 64px;
    line-height: 75px;
    text-align: center;
    letter-spacing: 0.5px;
    margin: 0;
    font-weight: 400;
  }
  .offer {
    position: absolute;
    left: 293px;
    top: 114px;
    width: 650px;
    height: 53px;
    background: var(--white);
    color: var(--ink);
    font-size: 35px;
    line-height: 53px;
    text-align: center;
    margin: 0;
  }
  .offer__price { color: var(--price); }
  .contact {
    position: absolute;
    left: 960px;
    top: 114px;
    color: var(--white);
    font-family: "Roboto Condensed", sans-serif;
    font-weight: 700;
    font-size: 22px;
    line-height: 28px;
    margin: 0;
  }
  .contact span { display: block; }
</style>
</head>
<body>
  <div class="banner">
    <div class="banner__flames" role="img" aria-label="Foto von lodernden Flammen als Hintergrund"></div>

    <div class="brand">
      <svg class="brand__circle" viewBox="0 0 90 90" aria-hidden="true">
        <circle cx="45" cy="45" r="42" fill="none" stroke="#ffffff" stroke-width="3"/>
      </svg>
      <p class="brand__name">Kaminholzhandel Lindqvist</p>
      <p class="brand__tagline">Feuer und Flamme für Berlin &amp; Brandenburg</p>
    </div>

    <h1 class="headline">KAMIN- &amp; BRENNHOLZ</h1>
    <p class="offer">ofenfertig gespalten schon <span class="offer__price">ab 49,- €</span></p>

    <p class="contact">
      <span class="contact__web">ofenscheit-lindqvist.de</span>
      <span class="contact__phone">Tel.: 030 55 41 27 06</span>
    </p>
  </div>
</body>
</html>
```